Dalton Power Supply, Inc. Business Card Design

We are an Electrical Distributor looking for a Modern, Professional Business Card design.

Target Market(s)

Residential Commercial Industrial

Industry/Entity Type

Electrical

Contact Information for Business Card

Dalton Power Supply, Inc.
418 Maple Ridge Lane
Brookvale, NC 27514
555-214-7630
555-214-8842 Fax
daltonpower@brightmail-example.net

```html
<!DOCTYPE html>
<html lang="en">
<head>
<meta charset="utf-8">
<title>Dalton Power Supply, Inc. – Business Card</title>
<link rel="stylesheet" href="https://fonts.googleapis.com/css2?family=Montserrat:wght@400;700;800&display=swap">
<style>
  :root {
    --page-bg: #e4e2de;
    --card-bg: #2c2d2f;
    --card-edge: #1f2022;
    --photo-light: #6a6b6d;
    --photo-dark: #2c2d2f;
    --text-white: #f4f4f4;
    --text-grey: #c9c9c9;
    --accent-blue: #27a3dc;
    --rule: #d9d9d9;
  }
  * { margin: 0; padding: 0; box-sizing: border-box; }
  html, body { width: 1200px; height: 1022px; overflow: hidden; }
  body {
    background: var(--page-bg);
    font-family: "Montserrat", Arial, sans-serif;
    display: flex; align-items: center; justify-content: center;
  }
  .card {
    position: relative;
    width: 1050px; height: 600px;
    background: linear-gradient(135deg, #38393b 0%, var(--card-bg) 55%, var(--card-edge) 100%);
    border-radius: 22px;
    overflow: hidden;
    box-shadow: 0 18px 40px rgba(0,0,0,.35);
  }
  .card__photo {
    position: absolute;
    left: 250px; top: 0;
    width: 560px; height: 600px;
    background: radial-gradient(ellipse at 45% 45%, var(--photo-light) 0%, #4a4b4d 35%, var(--photo-dark) 75%);
    opacity: .85;
  }
  .brand {
    position: absolute;
    left: 60px; top: 250px;
    display: flex; align-items: center; gap: 14px;
  }
  .brand__mark {
    width: 18px; height: 18px; border-radius: 50%;
    background: var(--accent-blue);
  }
  .brand__name {
    font-weight: 800; font-size: 34px; letter-spacing: .5px;
    color: var(--text-white);
    line-height: 1.1;
  }
  .person {
    position: absolute;
    right: 60px; top: 70px;
    text-align: right;
  }
  .person__name {
    font-weight: 800; font-size: 38px; letter-spacing: 1px;
    color: var(--text-white); text-transform: uppercase;
  }
  .person__title {
    margin-top: 6px;
    font-size: 20px; letter-spacing: 2px;
    color: var(--accent-blue); text-transform: uppercase;
  }
  .person__rule {
    position: absolute;
    right: 60px; top: 180px;
    width: 420px; height: 2px; background: var(--rule);
  }
  .address {
    position: absolute;
    right: 60px; top: 205px;
    text-align: right;
    font-size: 22px; line-height: 1.55;
    color: var(--text-grey);
  }
  .contact {
    position: absolute;
    right: 60px; bottom: 50px;
    width: 520px;
    border-top: 2px solid var(--rule);
    padding-top: 18px;
  }
  .contact__row {
    display: flex; align-items: center; gap: 14px;
    font-size: 22px; line-height: 1.5;
    color: var(--text-grey);
  }
  .contact__icon { width: 20px; height: 20px; flex: none; }
</style>
</head>
<body>
  <main class="card">
    <div class="card__photo" role="img" aria-label="Photo of a light bulb and electrical plug assembly beside a wall socket, in dark grey tones"></div>

    <div class="brand">
      <span class="brand__mark"></span>
      <span class="brand__name">Dalton Power Supply, Inc.</span>
    </div>

    <div class="person">
      <div class="person__name">Devon Harlow</div>
      <div class="person__title">Director</div>
    </div>
    <div class="person__rule"></div>
    <div class="address">
      418 Maple Ridge Lane<br>
      Brookvale, NC 27514
    </div>

    <div class="contact">
      <div class="contact__row">
        <svg class="contact__icon" viewBox="0 0 24 24" fill="none" stroke="#27a3dc" stroke-width="2"><path d="M5 3h4l2 5-2.5 1.5a11 11 0 0 0 6 6L16 13l5 2v4a2 2 0 0 1-2 2A16 16 0 0 1 3 5a2 2 0 0 1 2-2z"/></svg>
        <span>555-214-7630</span>
      </div>
      <div class="contact__row">
        <svg class="contact__icon" viewBox="0 0 24 24" fill="none" stroke="#27a3dc" stroke-width="2"><rect x="6" y="3" width="12" height="6"/><rect x="3" y="9" width="18" height="9" rx="1"/><rect x="7" y="15" width="10" height="6"/></svg>
        <span>555-214-8842</span>
      </div>
      <div class="contact__row">
        <svg class="contact__icon" viewBox="0 0 24 24" fill="none" stroke="#27a3dc" stroke-width="2"><rect x="3" y="5" width="18" height="14" rx="1"/><path d="M3 6l9 7 9-7"/></svg>
        <span>daltonpower@brightmail-example.net</span>
      </div>
    </div>
  </main>
</body>
</html>
```